Business Card Design

I already have a company logo for my company. I have a logo for the manufacturer we represent. I want a professional business card design.

```html
<!DOCTYPE html>
<html lang="en">
<head>
<meta charset="utf-8">
<title>Beacon Guard LLC – Business Card</title>
<link rel="stylesheet" href="https://fonts.googleapis.com/css2?family=Open+Sans:wght@400;600&display=swap">
<style>
  :root {
    --stage: #3a3a3a;
    --card: #161616;
    --red: #e31e26;
    --gold: #e0a823;
    --white: #f2f2f2;
  }
  * { box-sizing: border-box; margin: 0; padding: 0; }
  html, body { width: 1200px; height: 780px; overflow: hidden; }
  body {
    background: var(--stage);
    font-family: "Open Sans", Arial, sans-serif;
    display: flex;
    align-items: center;
    justify-content: center;
    gap: 40px;
  }
  .card {
    position: relative;
    width: 540px;
    height: 310px;
    background: var(--card);
    border-radius: 22px;
    overflow: hidden;
  }
  .brand {
    display: flex;
    align-items: center;
    gap: 10px;
    color: var(--white);
    font-weight: 600;
    letter-spacing: 1px;
    white-space: nowrap;
  }
  .brand-mark {
    width: 16px;
    height: 16px;
    background: var(--red);
    flex: none;
  }
  /* Front */
  .card-front .brand {
    position: absolute;
    left: 34px;
    top: 98px;
    font-size: 17px;
    letter-spacing: 0.5px;
  }
  .card-front .brand-mark { width: 14px; height: 14px; }
  .divider {
    position: absolute;
    left: 292px;
    top: 60px;
    width: 1px;
    height: 172px;
    background: var(--red);
  }
  .contact {
    position: absolute;
    left: 314px;
    top: 66px;
    color: var(--white);
    font-size: 14px;
    line-height: 1.5;
  }
  .contact-name {
    color: var(--red);
    font-size: 22px;
    font-weight: 600;
    line-height: 1.15;
    text-transform: uppercase;
  }
  .contact-role { font-size: 15px; margin-bottom: 6px; }
  .contact-line { display: flex; align-items: center; gap: 7px; }
  .contact-line svg { width: 12px; height: 12px; flex: none; fill: var(--red); }
  .contact-address { margin-top: 4px; }
  .edge-band {
    position: absolute;
    left: 0; right: 0; bottom: 0;
    height: 20px;
    display: flex;
  }
  .edge-band-gold { width: 45%; background: var(--gold); }
  .edge-band-red { flex: 1; background: var(--red); margin-left: 3px; }
  /* Back */
  .card-back {
    display: flex;
    align-items: center;
    justify-content: center;
  }
  .card-back .brand { font-size: 28px; gap: 14px; }
  .card-back .brand-mark { width: 22px; height: 22px; }
</style>
</head>
<body>
  <section class="card card-front">
    <div class="brand"><span class="brand-mark"></span><span>BEACON GUARD LLC</span></div>
    <div class="divider"></div>
    <div class="contact">
      <p class="contact-name">Daniel Reyes</p>
      <p class="contact-role">Managing Director</p>
      <p class="contact-line">
        <svg viewBox="0 0 24 24" aria-hidden="true"><path d="M6.6 10.8a15 15 0 0 0 6.6 6.6l2.2-2.2a1 1 0 0 1 1-.25 11.4 11.4 0 0 0 3.6.57 1 1 0 0 1 1 1V20a1 1 0 0 1-1 1A17 17 0 0 1 3 4a1 1 0 0 1 1-1h3.5a1 1 0 0 1 1 1c0 1.25.2 2.450.57 3.57a1 1 0 0 1-.25 1z"/></svg>
        123 456 789
      </p>
      <p class="contact-line">
        <svg viewBox="0 0 24 24" aria-hidden="true"><path d="M2 5h20v14H2z M4 7v.5l8 5 8-5V7l-8 5z" fill-rule="evenodd"/></svg>
        info@yourmail.com
      </p>
      <p class="contact-line">
        <svg viewBox="0 0 24 24" aria-hidden="true"><path d="M12 2a10 10 0 1 0 0 20 10 10 0 0 0 0-20zm6.9 6h-3a15 15 0 0 0-1.4-3.9A8 8 0 0 1 18.9 8zM12 4c.8 1.2 1.5 2.5 1.9 4h-3.8c.4-1.5 1.1-2.8 1.9-4zM4.3 14a8 8 0 0 1 0-4h3.4a16 16 0 0 0 0 4zm.8 2h3a15 15 0 0 0 1.4 3.9A8 8 0 0 1 5.1 16zm3-8h-3a8 8 0 0 1 4.4-3.9A15 15 0 0 0 8.1 8zM12 20c-.8-1.2-1.5-2.5-1.9-4h3.8c-.4 1.5-1.1 2.8-1.9 4zm2.3-6H9.7a14 14 0 0 1 0-4h4.6a14 14 0 0 1 0 4zm.2 5.9a15 15 0 0 0 1.4-3.9h3a8 8 0 0 1-4.4 3.9zm1.8-5.9a16 16 0 0 0 0-4h3.4a8 8 0 0 1 0 4z"/></svg>
        www.yourwebsite.com
      </p>
      <p class="contact-address">Your address, City<br>State, Zip 1234</p>
    </div>
    <div class="edge-band"><span class="edge-band-gold"></span><span class="edge-band-red"></span></div>
  </section>

  <section class="card card-back">
    <div class="brand"><span class="brand-mark"></span><span>BEACON GUARD LLC</span></div>
  </section>
</body>
</html>
```